Website design for headhunting agency

The design I need (PSD file) is for a company offering specialised services in recruitment of high-end executive and management positions for businesses.
OBJECTIVES OF THE WEBSITE:
1. Let entrepreneurs and business leaders know about their services and easily have them contact Velnarix if they want more information about their services.
2. Display a list of available carreer opportunities (according to their client's need).
WHAT I NEED:
1st, I need the design for the Home Page ONLY. Once approved, I will need the other pages designed as well. (Here is prototype that we've already developed for the Website that will guide you in the design:
http://demo.quorvaweb.example/velnarix/fr/accueil)
ATTACHED FILES
- Logo
- PDF brochure: Use for inspiration. It is encouraged that you use pictures from this brochure. You can always suggest new ones, as long as they are not expensive to buy and have the same look and feel as the brochure.
HOMEPAGE:
1. Main menu : 6 sections
Accueil | Velnarix | Équipe | Approche | Postes disponibles | Publications
2. Main slider: 4 sections
- Chasseurs de têtes (Headhunters)
- Notre approche (Our Approach)
- Postes cadres disponibles (Executive Careers
Opportunities)
- Contactez-nous (Contact Us)
3. Main Call To Action Boxes :
- Liste Des postes disponibles (Liste of Available Careers
Opportunities)
- Formulaire de contact (contact form)
4. Latest blog articles
- Les derniers articles.
OTHER PAGES (to design once Homepage is approved)
- Velnarix (about us)
- Équipe (our team)
- Approche (our approach)
- Postes disponibles (Career opportunities)
- Publications (blog articles)
- Contact (Contact us)
Target Market(s)
ORGANIZATIONS:
Leaders of organizations seeking to recruit highly qualified staff.
HIGHLY QUALIFIED RESOURCES:
Senior individuals seeking a salary between $70,000 and $ $200,000 annually
PROFESSIONAL SECTORS:
manufacturing : Primary and secondary industries
pharmaceutical
Aerospace
Finances
Retail business
Engineering
Chemical and petrochemical
IT, telecommunications and high technology
Professional Organizations and Association
Industry/Entity Type
Business
Look and feel
Each slider illustrates characteristics of the customer's brand and the style your logo design should communicate.

```html
<!DOCTYPE html>
<html lang="fr">
<head>
<meta charset="utf-8">
<title>Velnarix – Accueil</title>
<link rel="stylesheet" href="https://fonts.googleapis.com/css2?family=Raleway:wght@400;500;600&display=swap">
<style>
  :root {
    --page-bg: #f5f4f1;
    --page-band: #efeeea;
    --footer-band: #e6e5e2;
    --teal-dark: #10262a;
    --teal-mid: #234d53;
    --teal-light: #2f6168;
    --accent: #e2a038;
    --heading: #3a3f44;
    --muted: #9a9a9a;
    --rule: #e4e3e0;
    --card: #f7f6f3;
  }
  * { box-sizing: border-box; margin: 0; padding: 0; }
  html, body { width: 1200px; height: 899px; overflow: hidden; }
  body {
    position: relative;
    background: var(--page-bg);
    font-family: "Raleway", Arial, sans-serif;
  }
  .backdrop { position: absolute; inset: 0; }
  .hero-cta {
    position: absolute; left: 0; width: 1200px; top: 23px;
    display: flex; flex-direction: column; align-items: center;
    color: var(--accent); text-decoration: none;
  }
  .hero-cta-icon {
    width: 52px; height: 52px; border: 2px solid var(--accent); border-radius: 50%;
    display: flex; align-items: center; justify-content: center;
    font-size: 22px; font-weight: 600;
  }
  .hero-cta-label { margin-top: 7px; font-size: 18px; font-weight: 500; }
  .slider-dots { position: absolute; top: 208px; left: 546px; display: flex; gap: 16px; }
  .slider-dot {
    width: 14px; height: 14px; border-radius: 50%;
    background: #1d3f44; border: 1px solid #3d6a70;
  }
  .slider-dot.is-active { background: #fff; border-color: #fff; transform: scale(.8); }

  .section-title {
    position: absolute; top: 276px;
    font-size: 19px; font-weight: 500; color: var(--heading);
    padding-left: 17px;
  }
  .section-title::before {
    content: ""; position: absolute; left: 0; top: 5px;
    border-left: 7px solid var(--accent);
    border-top: 7px solid transparent; border-bottom: 7px solid transparent;
  }
  .card {
    position: absolute; top: 314px; width: 347px; height: 437px;
    background: var(--card);
    box-shadow: 0 1px 4px rgba(0,0,0,.15);
    overflow: hidden;
  }
  .jobs-card { left: 221px; border-bottom: 5px solid var(--accent); }
  .jobs-photo {
    height: 166px;
    background: linear-gradient(160deg, #d8d8d8 0%, #8c8c8c 40%, #3e3e3e 75%, #b5b5b5 100%);
  }
  .job-list { list-style: none; padding: 0 24px; }
  .job-item {
    height: 52px; display: flex; align-items: center; justify-content: space-between;
    font-size: 12px; color: var(--muted); border-bottom: 1px solid var(--rule);
    padding: 0 13px 0 1px;
  }
  .job-item:last-child { border-bottom: none; }
  .job-arrow {
    width: 24px; height: 24px; border-radius: 50%; background: var(--accent);
    display: flex; align-items: center; justify-content: center;
  }
  .more-jobs {
    position: absolute; left: 245px; top: 768px;
    display: flex; align-items: center; gap: 9px;
    font-size: 12px; font-weight: 500; color: var(--accent);
  }
  .more-jobs-icon {
    width: 25px; height: 25px; border: 2px solid var(--accent); border-radius: 50%;
    display: flex; align-items: center; justify-content: center; font-size: 13px; font-weight: 600;
  }
  .contact-card { left: 632px; }
  .contact-form { padding: 14px 22px 0 24px; }
  .form-field {
    height: 52px; display: flex; align-items: center;
    font-size: 12px; color: var(--muted); border-bottom: 1px solid var(--rule);
  }
  .form-field:last-of-type { border-bottom: none; }
  .form-submit {
    position: absolute; left: 0; bottom: 0; width: 100%; height: 55px;
    background: var(--accent); color: #fff; border: none;
    font-family: "Raleway", Arial, sans-serif; font-size: 17px; font-weight: 500;
  }
</style>
</head>
<body>
  <svg class="backdrop" width="1200" height="899" viewBox="0 0 1200 899">
    <defs>
      <linearGradient id="heroTone" x1="0" y1="0" x2="1" y2="0.4">
        <stop offset="0" stop-color="#0c1c1f"/>
        <stop offset="0.3" stop-color="#2a5a60"/>
        <stop offset="0.6" stop-color="#1f484e"/>
        <stop offset="1" stop-color="#0e2226"/>
      </linearGradient>
    </defs>
    <polygon points="0,282 600,242 1200,282 1200,899 0,899" fill="var(--page-band)"/>
    <polygon points="0,0 1200,0 1200,135 600,242 0,138" fill="url(#heroTone)"
      role="img" aria-label="Photo de salle de réunion avec documents sur la table, teintée bleu sarcelle"/>
    <polygon points="430,215 600,187 770,215 600,242" fill="#2c5f66" opacity=".8"/>
    <polygon points="90,899 600,810 1110,899" fill="var(--footer-band)"/>
  </svg>

  <a class="hero-cta" href="#">
    <span class="hero-cta-icon">+</span>
    <span class="hero-cta-label">En savoir plus</span>
  </a>
  <div class="slider-dots">
    <span class="slider-dot"></span>
    <span class="slider-dot"></span>
    <span class="slider-dot is-active"></span>
    <span class="slider-dot"></span>
  </div>

  <h2 class="section-title" style="left:221px">Liste des postes disponibles</h2>
  <section class="card jobs-card">
    <div class="jobs-photo" role="img" aria-label="Photo en noir et blanc d’une salle de conseil avec fauteuils et documents"></div>
    <ul class="job-list">
      <li class="job-item">Lorem ipsum.... <span class="job-arrow"><svg width="8" height="10" viewBox="0 0 8 10"><path d="M2 1l4 4-4 4" fill="none" stroke="#fff" stroke-width="1.3"/></svg></span></li>
      <li class="job-item">Lorem ipsum.... <span class="job-arrow"><svg width="8" height="10" viewBox="0 0 8 10"><path d="M2 1l4 4-4 4" fill="none" stroke="#fff" stroke-width="1.3"/></svg></span></li>
      <li class="job-item">Lorem ipsum.... <span class="job-arrow"><svg width="8" height="10" viewBox="0 0 8 10"><path d="M2 1l4 4-4 4" fill="none" stroke="#fff" stroke-width="1.3"/></svg></span></li>
      <li class="job-item">Lorem ipsum.... <span class="job-arrow"><svg width="8" height="10" viewBox="0 0 8 10"><path d="M2 1l4 4-4 4" fill="none" stroke="#fff" stroke-width="1.3"/></svg></span></li>
      <li class="job-item">Lorem ipsum.... <span class="job-arrow"><svg width="8" height="10" viewBox="0 0 8 10"><path d="M2 1l4 4-4 4" fill="none" stroke="#fff" stroke-width="1.3"/></svg></span></li>
    </ul>
  </section>
  <a class="more-jobs" href="#"><span class="more-jobs-icon">+</span>Plus de postes</a>

  <h2 class="section-title" style="left:632px">Formulaire de contact</h2>
  <section class="card contact-card">
    <form class="contact-form">
      <label class="form-field">Nom:</label>
      <label class="form-field">Prénom(s):</label>
      <label class="form-field">Date de naissance:</label>
      <label class="form-field">Adresse:</label>
      <label class="form-field">Poste actuel:</label>
      <label class="form-field">Téléphone:</label>
      <label class="form-field">Email:</label>
      <button class="form-submit" type="button">Je m’inscris</button>
    </form>
  </section>
</body>
</html>
```